Business card design needed

I run a Beautician studio (for 7 years now)
I offer
- Vestolin Body Sugaring
- Velumi Glow
- Nails
- Facials
- Manicure
- Foot Treatment
It might not be necessary to list all those treatments?
Maybe the link to the Website is sufficient?
I leave that up to you ...
(more info on www.BuffsAndBrowsByMarisol.com.au)
Vestolin BodySugaring is our biggest success, It replaces waxing.
I would like to incorporate the logo into the Business Card.
We had many complaints regarding our old Business Cards as the Phone Number was to small.
On the backside, we would like a "your next Appointment" section.
Looking forward to you Design, cheers ... Marisol
Buffs by Brows by Marisol
14 Merindo Cct 3912 Kellmoor
www.BuffsAndBrowsByMarisol.com.au
03 9418 2276

```html
<!DOCTYPE html>
<html lang="en">
<head>
<meta charset="utf-8">
<title>Vestolin Body Sugaring – Business Card</title>
<link rel="stylesheet" href="https://fonts.googleapis.com/css2?family=Arimo:wght@400;700&display=swap">
<style>
  :root {
    --backdrop: #979795;
    --card: #ffffff;
    --ink: #1e1e1e;
    --muted: #9a9a9a;
    --rule: #222222;
    --accent: #f29a1e;
  }
  html, body {
    margin: 0;
    width: 1200px;
    height: 1000px;
    overflow: hidden;
    background: var(--backdrop);
    font-family: "Arimo", Arial, sans-serif;
  }
  .card {
    position: absolute;
    left: 382px;
    top: 128px;
    width: 468px;
    height: 798px;
    background: var(--card);
    color: var(--ink);
  }
  .card > * { position: absolute; left: 0; width: 100%; margin: 0; text-align: center; }
  .holder-name { top: 40px; font-size: 24px; font-weight: 700; }
  .brand { top: 250px; }
  .brand-dot {
    display: block;
    width: 70px; height: 70px;
    margin: 0 auto 26px;
    border-radius: 50%;
    background: var(--accent);
  }
  .brand-name { font-size: 30px; font-weight: 400; letter-spacing: 1px; color: var(--ink); }
  .studio { top: 550px; font-size: 22px; line-height: 31px; }
  .studio .lead { color: var(--muted); }
  .divider {
    top: 632px; left: 13px; width: 442px; height: 0;
    border-top: 2px solid var(--rule);
  }
  .booking { top: 645px; font-size: 22px; line-height: 28px; }
  .booking .lead { color: var(--muted); }
  .booking .phone { font-weight: 700; }
  .website { top: 748px; font-size: 20px; font-weight: 700; }
</style>
</head>
<body>
  <main class="card">
    <p class="holder-name">Marisol Kendrew</p>

    <div class="brand">
      <span class="brand-dot"></span>
      <span class="brand-name">Vestolin Body Sugaring</span>
    </div>

    <p class="studio">
      <span class="lead">Buffs by Brows by</span><br>
      Marisol 14 Merindo Cct 3912 Kellmoor
    </p>

    <div class="divider"></div>

    <p class="booking">
      <span class="lead">For appointments please call -</span><br>
      <span class="phone">Tel 03 9418 2276</span>
    </p>

    <p class="website">www.buffsandbrowsbymarisol.com.au</p>
  </main>
</body>
</html>
```